Business Card Design for Lawn Management

Lawn Management

Industry/Entity Type

Business

Contact Information for Business Card

Calloway Lawn Management
Doran Calloway
Calloway_Lawn@brindlemail.com
404-627-1845

```html
<!DOCTYPE html>
<html lang="en">
<head>
<meta charset="utf-8">
<title>Calloway Lawn Management – Business Cards</title>
<link rel="stylesheet" href="https://fonts.googleapis.com/css2?family=Poiret+One&display=swap">
<style>
  :root {
    --backdrop: #e9e6e1;
    --lawn-dark: #2f5a1f;
    --lawn-mid: #3f7229;
    --lawn-light: #4c8232;
    --ink-light: #f4f6ef;
    --panel-tint: rgba(255, 255, 255, 0.32);
    --card-edge: #ffffff;
  }
  * { box-sizing: border-box; margin: 0; padding: 0; }
  html, body {
    width: 1200px;
    height: 550px;
    overflow: hidden;
    background: var(--backdrop);
  }
  .canvas {
    position: relative;
    width: 1200px;
    height: 550px;
    display: flex;
    align-items: center;
    justify-content: center;
    gap: 60px;
  }
  .card {
    position: relative;
    width: 510px;
    height: 290px;
    border-radius: 3px;
    overflow: hidden;
    box-shadow: 0 2px 0 var(--card-edge), 0 6px 14px rgba(0, 0, 0, 0.18);
    color: var(--ink-light);
    font-family: "Poiret One", sans-serif;
  }
  .lawn-texture {
    position: absolute;
    inset: 0;
    background: radial-gradient(ellipse at 40% 35%, var(--lawn-light), var(--lawn-mid) 55%, var(--lawn-dark));
  }
  .brand {
    position: absolute;
    display: flex;
    align-items: flex-end;
    gap: 10px;
  }
  .brand-name {
    font-size: 30px;
    font-variant: small-caps;
    letter-spacing: 1.5px;
    line-height: 1;
    padding: 0 4px 6px;
    border-bottom: 1.5px solid var(--ink-light);
    white-space: nowrap;
  }
  .brand-mark {
    width: 16px;
    height: 16px;
    background: var(--ink-light);
    margin-bottom: 4px;
  }
  /* Front */
  .card-front .brand { left: 30px; bottom: 62px; }
  .front-phone {
    position: absolute;
    right: 66px;
    bottom: 36px;
    font-size: 15px;
    letter-spacing: 1.5px;
  }
  /* Back */
  .card-back .brand { left: 30px; top: 60px; }
  .contact-panel {
    position: absolute;
    right: 16px;
    bottom: 52px;
    width: 210px;
    padding: 10px 12px;
    background: var(--panel-tint);
    display: flex;
    flex-direction: column;
    gap: 4px;
  }
  .contact-row {
    display: flex;
    align-items: center;
    gap: 8px;
    white-space: nowrap;
  }
  .contact-row svg { width: 13px; height: 13px; flex: none; fill: var(--ink-light); }
  .contact-name { font-size: 19px; letter-spacing: 0.5px; }
  .contact-email { font-size: 10.5px; }
  .contact-phone { font-size: 13px; letter-spacing: 1px; }
</style>
</head>
<body>
<main class="canvas">
  <section class="card card-front">
    <div class="lawn-texture" role="img" aria-label="Close-up green grass texture"></div>
    <div class="brand">
      <span class="brand-name">Calloway Lawn Management</span>
      <span class="brand-mark"></span>
    </div>
    <p class="front-phone">404-627-1845</p>
  </section>

  <section class="card card-back">
    <div class="lawn-texture" role="img" aria-label="Close-up green grass texture"></div>
    <div class="brand">
      <span class="brand-name">Calloway Lawn Management</span>
      <span class="brand-mark"></span>
    </div>
    <address class="contact-panel">
      <div class="contact-row contact-name">
        <svg viewBox="0 0 16 16" aria-hidden="true"><circle cx="8" cy="4.5" r="3.5"/><path d="M1 16c0-4 3-7 7-7s7 3 7 7z"/></svg>
        <span>Doran Calloway</span>
      </div>
      <div class="contact-row contact-email">
        <svg viewBox="0 0 16 16" aria-hidden="true"><text x="0" y="13" font-size="15" font-family="sans-serif" font-weight="bold">@</text></svg>
        <span>Calloway_Lawn@brindlemail.com</span>
      </div>
      <div class="contact-row contact-phone">
        <svg viewBox="0 0 16 16" aria-hidden="true"><path d="M3.5 1l3 3-1.8 2a9 9 0 0 0 5.3 5.3l2-1.8 3 3-2 2.5C6 14.5 1.5 10 1 3z"/></svg>
        <span>404-627-1845</span>
      </div>
    </address>
  </section>
</main>
</body>
</html>
```